Family owned plumbing contractor needs eye catching business card design

Business cards that are unique, eye catching, and provide customers with general company information, such as name, address, phone number, website, employee name/title, cell phone #, & email address. We are transitioning to a new logo that utilizes a more retro feel, so we are interested in seeing some cool old school designs in the mix. We are liking the dark background on some of the samples on this website. If that is workable with our artwork, we would like to see that incorporated into the design.
Contact Information for Business Card
Copperline Pipeworks, Inc.
www.copperlinepipeworks.example
(555) 630-2918 phone
Nevada License #64205
California License #5870413
Glen Harwick, President
(555) 418-9063 cell
glen@copperlinepipeworks.example
Residential * Commercial * Service
Requirements
Must have
- The business card details listed above & logo provided.
Nice to have
- I made some notes about color options in the description.

```html
<!DOCTYPE html>
<html lang="en">
<head>
<meta charset="utf-8">
<title>Copperline Pipeworks, Inc. – Business Card</title>
<link rel="stylesheet" href="https://fonts.googleapis.com/css2?family=Montserrat:wght@400;500;600&display=swap">
<style>
  :root {
    --stage: #2e2723;
    --slate: #587b95;
    --slate-deep: #4b6b84;
    --mint: #76c5b1;
    --white: #ffffff;
    --ink: #eef4f7;
  }
  html, body {
    margin: 0;
    padding: 0;
    width: 1200px;
    height: 831px;
    overflow: hidden;
    background: var(--stage);
    font-family: "Montserrat", Arial, sans-serif;
  }
  .canvas {
    position: relative;
    width: 1200px;
    height: 831px;
  }
  .card {
    position: absolute;
    width: 540px;
    height: 309px;
    background: linear-gradient(135deg, var(--slate) 0%, var(--slate-deep) 100%);
    border-radius: 4px;
    overflow: hidden;
    box-shadow: 0 18px 40px rgba(0,0,0,0.45);
    color: var(--ink);
  }
  .card--front { left: 45px; top: 120px; }
  .card--back  { left: 615px; top: 380px; }

  /* brand lockup: name set in the card's own type, with one plain circle */
  .brand {
    position: absolute;
    display: flex;
    align-items: center;
    gap: 14px;
  }
  .brand__dot {
    flex: none;
    width: 34px;
    height: 34px;
    border-radius: 50%;
    background: var(--mint);
  }
  .brand__name {
    font-weight: 600;
    color: var(--white);
    line-height: 1.15;
  }
  .card--front .brand { left: 120px; top: 118px; }
  .card--front .brand__name { font-size: 26px; }

  .card--back .brand { left: 40px; top: 112px; gap: 10px; }
  .card--back .brand__dot { width: 24px; height: 24px; }
  .card--back .brand__name { font-size: 18px; }

  .services {
    position: absolute;
    left: 26px;
    top: 18px;
    font-size: 13px;
    line-height: 1.4;
  }
  .licenses {
    position: absolute;
    left: 26px;
    top: 214px;
    font-size: 12px;
    line-height: 1.35;
  }
  .flames {
    position: absolute;
    right: 0;
    top: 70px;
    width: 250px;
    height: 150px;
    background: linear-gradient(90deg, rgba(118,197,177,0) 0%, var(--mint) 45%, var(--mint) 100%);
    border-radius: 80px 0 0 80px;
  }
  .person {
    position: absolute;
    right: 28px;
    top: 100px;
    text-align: right;
    color: var(--white);
  }
  .person__name {
    font-size: 19px;
    font-weight: 600;
    letter-spacing: 0.04em;
    text-transform: uppercase;
  }
  .person__title {
    font-size: 12px;
  }
  .contact {
    position: absolute;
    font-size: 12.5px;
    line-height: 1.4;
  }
  .contact--online { left: 200px; top: 250px; }
  .contact--phones { right: 28px; top: 214px; text-align: left; }
  .edge-band {
    position: absolute;
    left: 0;
    right: 0;
    bottom: 0;
    height: 8px;
    background: var(--mint);
  }
</style>
</head>
<body>
<main class="canvas">

  <section class="card card--front" aria-label="Card front">
    <div class="brand">
      <span class="brand__dot"></span>
      <span class="brand__name">Copperline<br>Pipeworks, Inc.</span>
    </div>
  </section>

  <section class="card card--back" aria-label="Card back">
    <div class="services">Residential<br>Commercial | Service</div>

    <div class="brand">
      <span class="brand__dot"></span>
      <span class="brand__name">Copperline<br>Pipeworks, Inc.</span>
    </div>

    <div class="licenses">Nevada License #64205<br>California License #5870413</div>

    <div class="flames" role="img" aria-label="Mint flame illustration sweeping in from the right edge"></div>

    <div class="person">
      <div class="person__name">Glen Harwick</div>
      <div class="person__title">President</div>
    </div>

    <div class="contact contact--phones">P: (555) 630-2918<br>C: (555) 418-9063</div>
    <div class="contact contact--online">glen@copperlinepipeworks.example<br>www.copperlinepipeworks.example</div>

    <div class="edge-band"></div>
  </section>

</main>
</body>
</html>
```